Business card design needed

I need a business card for a new company based in Perth, Western Australia, called KT Power Pty Ltd.

I'm the sole proprietor, and have 25 years' experience in directorship, senior commercial/business development/strategy roles in the oil & gas industry with both supermajors and junior listed companies. I also have interests in renewable energy (and am co-founder and director of a separate renewable energy start-up company). KT Power will be the vehicle for me to contract my services, principally in the oil & gas industry (although this will include directorship services to the renewable energy company). These services will include general consultancy in my areas of expertise, and contracting to provide senior management/director services to start-up or junior oil and gas companies.

I'm looking for a design that communicates professionalism, dynamism, experience, strategic skills and growth.

My ConnectHub profile may also be useful context;

"I have a real passion for discovering new investment opportunities and turning them from talk into reality. Right now my focus is on oil, gas and energy ventures. I’m always on the look out for compelling new investment opportunities where I can bring my leadership and strategic insight to bear to make a real difference by delivering transformational results.

I spent 24 years with HX where I built up extensive international experience in oil, gas and energy and was a member of the company’s “fast track” development programme. As an entrepreneurial senior commercial leader, strategic thinker and tactical dealmaker I was responsible for numerous deals such as divestments, farm-ins, asset swaps, new acreage bids, unitizations, gas and LNG sales, creating billions of dollars of value for HX. These deals frequently broke new ground and/or required an innovative approach that delivered results in excess of what the business thought achievable. I have held senior executive and director roles covering Exploration & Production, Mergers & Acquisitions, Business Development, LNG Marketing, Joint Venture Management, Gas & Power and Corporate head office. International assignments included UK, Australia, Indonesia, Norway & Belgium.

I’m a member of the Guild of Global Fuel Brokers (GGFB) and the Southern Council of Board Members (SCBM).

Board experience comprises four directorships and two alternate directorships of Australian companies, and directorship of a Not for Profit organisation.

Specialties
Strategy, Business Development, Mergers & Acquisitions, Joint Venture Management, Negotiation, Gas & LNG Marketing."

Target Market(s)

Oil and gas or energy companies of all sizes from large listed companies to start-ups - also service providers to the industry.

Industry/Entity Type

Oil And Gas

Contact Information for Business Card

KT Power Pty Ltd
Daniel Hobart
27C Lorne Avenue,
Kelmsdale,
WA 6093

Tel +61 455 823 617
email hobartdk@vellimo.net.au

```html
<!DOCTYPE html>
<html lang="en">
<head>
<meta charset="utf-8">
<title>KT Power Pty Ltd – Business Card</title>
<link rel="stylesheet" href="https://fonts.googleapis.com/css2?family=Alegreya+Sans:wght@400;700&display=swap">
<style>
  :root {
    --backdrop: #e9e6e1;
    --card-white: #ffffff;
    --navy-deep: #082f5e;
    --navy-mid: #163f70;
    --navy-haze: #2a5583;
    --brand-blue: #1d4a7c;
    --rule-dark: #0a2f5a;
    --rule-light: #a9cbe2;
    --accent-sky: #c9e7f8;
    --text-white: #ffffff;
  }
  * { margin: 0; padding: 0; box-sizing: border-box; }
  html, body {
    width: 1200px; height: 799px; overflow: hidden;
    background: var(--backdrop);
    font-family: "Alegreya Sans", sans-serif;
  }
  .card {
    position: absolute; left: 80px; top: 110px;
    width: 1040px; height: 579px;
    background: var(--card-white);
    overflow: hidden;
    box-shadow: 0 6px 24px rgba(0,0,0,0.18);
  }
  .card-header {
    position: absolute; left: 0; top: 0; width: 100%; height: 172px;
    display: flex; align-items: center; justify-content: center;
  }
  .company-name {
    color: var(--brand-blue);
    font-weight: 400; font-size: 60px; letter-spacing: 0.5px;
  }
  .company-name .suffix { font-size: 36px; }
  .card-body {
    position: absolute; left: 0; top: 172px; width: 100%; height: 407px;
    background: var(--navy-deep);
  }
  .plant-backdrop {
    position: absolute; inset: 0;
    background:
      radial-gradient(ellipse at 42% 40%, rgba(80,120,165,0.35), transparent 55%),
      linear-gradient(180deg, var(--navy-deep) 0%, var(--navy-mid) 55%, var(--navy-haze) 100%);
  }
  .rule-dark { position: absolute; left: 0; top: 0; width: 100%; height: 4px; background: var(--rule-dark); }
  .rule-light { position: absolute; left: 0; top: 18px; width: 100%; height: 3px; background: var(--rule-light); }
  .person-name {
    position: absolute; left: 0; top: 82px; width: 100%;
    text-align: center; color: var(--text-white);
    font-weight: 700; font-size: 44px;
  }
  .contact-list {
    position: absolute; left: 270px; top: 244px; list-style: none;
    color: var(--text-white); font-size: 29px; line-height: 39px;
  }
  .contact-list li { display: flex; align-items: center; }
  .contact-list svg { width: 34px; height: 26px; margin-right: 4px; flex: none; }
  .accent-square {
    position: absolute; left: 0; bottom: 0; width: 88px; height: 88px;
    background: var(--accent-sky);
  }
</style>
</head>
<body>
  <div class="card">
    <header class="card-header">
      <h1 class="company-name">KT Power Pty <span class="suffix">Ltd.</span></h1>
    </header>
    <section class="card-body">
      <div class="plant-backdrop" role="img" aria-label="Faint photograph of a gas power plant with chimneys and tanks in navy tones"></div>
      <div class="rule-dark"></div>
      <div class="rule-light"></div>
      <h2 class="person-name">Daniel Hobart</h2>
      <ul class="contact-list">
        <li>
          <svg viewBox="0 0 34 26" aria-hidden="true"><circle cx="17" cy="8" r="4" fill="none" stroke="#fff" stroke-width="2.2"/><line x1="17" y1="12" x2="17" y2="22" stroke="#fff" stroke-width="2.2"/></svg>
          27C Lorne Avenue, Kelmsdale, WA 6093
        </li>
        <li>
          <svg viewBox="0 0 34 26" aria-hidden="true"><circle cx="16" cy="13" r="11" fill="none" stroke="#fff" stroke-width="1.8"/><path d="M11 8 q1-2 3 0 l1 2 q0 1-1 2 q1 3 4 4 q1-1 2-1 l2 1 q2 2 0 3 q-3 2-7-1 q-4-3-4-7z" fill="#fff"/></svg>
          Tel +61 455 823 617
        </li>
        <li>
          <svg viewBox="0 0 34 26" aria-hidden="true"><rect x="2" y="5" width="28" height="17" fill="#fff"/><path d="M2 5 L16 15 L30 5" fill="none" stroke="#163f70" stroke-width="2"/></svg>
          hobartdk@vellimo.net.au
        </li>
      </ul>
      <div class="accent-square" style="height:88px"></div>
    </section>
  </div>
</body>
</html>
```